New Word Template Design Project

I want design about template plant date palm tree
The size is A4/Users/mibu/Desktop/DSC07540.JPG
/Users/mibu/Desktop/DSC07514.JPG

```html
<!DOCTYPE html>
<html lang="en">
<head>
<meta charset="utf-8">
<title>Plant Date Palm Tree</title>
<link href="https://fonts.googleapis.com/css2?family=Montserrat:wght@700&family=Carlito&display=swap" rel="stylesheet">
<style>
  :root {
    --paper: #ffffff;
    --sky-top: #1ab4ee;
    --sky-mid: #5cc6ef;
    --palm-green: #7d9a4a;
    --palm-dark: #5a6b2e;
    --ground: #3f8d2c;
    --frame: #ffffff;
    --title-white: #ffffff;
    --title-blue: #27c4ef;
    --title-green: #92d050;
    --body-ink: #111111;
  }
  * { margin: 0; padding: 0; box-sizing: border-box; }
  html, body { width: 871px; height: 1200px; overflow: hidden; background: var(--paper); }
  .page {
    position: relative;
    width: 871px;
    height: 1200px;
    background: var(--paper);
    overflow: hidden;
  }
  .hero-photo {
    position: absolute;
    left: 0; top: 0;
    width: 871px; height: 667px;
    background: linear-gradient(180deg,
      var(--sky-top) 0%,
      var(--sky-mid) 30%,
      var(--palm-green) 52%,
      var(--palm-dark) 82%,
      var(--ground) 100%);
  }
  .hero-frame {
    position: absolute;
    left: 40px; top: 30px;
    width: 793px; height: 640px;
    border: 2px solid var(--frame);
    border-bottom: none;
  }
  .title-block {
    position: absolute;
    left: 0; top: 0;
    width: 871px; height: 1000px;
  }
  .title-block text {
    font-family: 'Montserrat', sans-serif;
    font-weight: 700;
  }
  .title-plant { fill: var(--title-white); }
  .title-date-palm { fill: var(--title-blue); }
  .title-tree { fill: var(--title-green); }
  .intro-text {
    position: absolute;
    left: 80px; top: 995px;
    width: 711px;
    font-family: 'Carlito', sans-serif;
    font-size: 14.2px;
    line-height: 21.7px;
    color: var(--body-ink);
    text-align: center;
  }
</style>
</head>
<body>
<main class="page">
  <div class="hero-photo" role="img" aria-label="Photograph of a date palm grove with tall palms under a blue sky with white clouds"></div>
  <div class="hero-frame"></div>

  <svg class="title-block" width="871" height="1000" viewBox="0 0 871 1000" aria-label="Plant date palm tree">
    <text class="title-plant" x="183" y="667" font-size="164" textLength="515" lengthAdjust="spacingAndGlyphs">PLANT</text>
    <text class="title-date-palm" x="183" y="762" font-size="98" textLength="514" lengthAdjust="spacingAndGlyphs">DATE PALM</text>
    <text class="title-tree" x="183" y="955" font-size="215" textLength="514" lengthAdjust="spacingAndGlyphs">TREE</text>
  </svg>

  <p class="intro-text">Lorem ipsum dolor sit amet, consectetur adipiscing elit. Donec accumsan consectetur tellus lobortis sodales. Nullam hendrerit, ligula ac finibus convallis, mauris leo ultrices purus, eget venenatis ex neque sed est. Integer risus elit, mattis a suscipit id, rhoncus eget lectus. Pellentesque varius a erat sit amet mollis. In purus augue, tincidunt sed efficitur vel, convallis mollis nisl. Fusce vulputate dolor non lorem vestibulum, quis blandit nulla mattis.</p>
</main>
</body>
</html>
```